Pitch deck power point presentation template

I need a power point template for a pitch deck for a startup biotechnology company using the logo we purchased from tallyvane. It should have a cover page and content pages that we can adapt to fit multiple presentations. It should have a page for the team and advisors, and pages for graphs and charts, also pages that have space to add pictures to give background information, and then some with general pages with some blank space. I want it to catch the eye but also be very professional looking.
Updates

The original deadline was only one day from posting for some reason, I extended to 5 days to allow more time.

Target Market(s)

Investors

Industry/Entity Type

Biotechnology

Font styles to use
Serif
Sans Serif

Colors
0054AA
0677BA
7BADD7
CADEEF
E8F1F8

Requirements
Must have
• The logo and the blue color from the logo as the primary color used
Nice to have
• other layouts that we can select from

```html
<!DOCTYPE html>
<html lang="en">
<head>
<meta charset="utf-8">
<title>Corvane Biosciences – Pitch Deck Template</title>
<link href="https://fonts.googleapis.com/css2?family=Montserrat:wght@400;500;600;700;800&family=Open+Sans:wght@400;600&display=swap" rel="stylesheet">
<style>
:root{
  --stage:#5e6166;
  --paper:#ffffff;
  --teal:#13a38b;
  --blue:#0a9bd8;
  --blue-deep:#0677ba;
  --sky:#cadeef;
  --mist:#e8f1f8;
  --grey-box:#e4e6e8;
  --ink:#3a3a3a;
  --muted:#6b6b6b;
}
*{margin:0;padding:0;box-sizing:border-box}
html,body{width:1200px;height:963px;overflow:hidden;background:var(--stage)}
body{position:relative;font-family:"Open Sans",Arial,sans-serif;color:var(--ink)}
.slide{position:absolute;width:372px;height:209px;background:var(--paper);overflow:hidden;box-shadow:0 3px 7px rgba(0,0,0,.45)}
.c1{left:28px}.c2{left:414px}.c3{left:800px}
.r1{top:38px}.r2{top:265px}.r3{top:490px}.r4{top:716px}
.abs{position:absolute}
.head{font-family:"Montserrat",Arial,sans-serif;line-height:1.05}
.brand{position:absolute;right:8px;top:10px;display:flex;align-items:center;gap:3px;font-family:"Montserrat",sans-serif;font-weight:700;color:var(--teal);font-size:10px;line-height:1}
.brand i{width:7px;height:7px;border-radius:50%;background:var(--teal);display:block}
.pageno{position:absolute;right:10px;bottom:6px;width:20px;height:20px;border:1.5px solid var(--teal);border-radius:50%;font:700 6px "Montserrat",sans-serif;color:var(--teal);display:flex;align-items:center;justify-content:center}
.photo{position:absolute}
.tiny{font-size:3.6px;line-height:1.35;color:var(--muted)}
.small{font-size:4.4px;line-height:1.4;color:var(--muted)}
.t-blue{color:var(--blue)}.t-teal{color:var(--teal)}
.bold{font-weight:800}
/* cover */
.cover-photo{right:0;top:0;width:270px;height:209px;background:linear-gradient(100deg,#fff 0%,#e8f1f8 30%,#a9d2ef 70%,#7badd7 100%)}
.cover-brand{left:18px;top:22px;display:flex;align-items:center;gap:6px;font:700 22px/1 "Montserrat",sans-serif;color:var(--teal)}
.cover-brand i{width:16px;height:16px;border-radius:50%;background:var(--teal);display:block}
/* contents */
.toc-item{position:absolute;left:232px;width:120px}
.toc-item b{display:block;font:700 7px "Montserrat",sans-serif;color:var(--teal);margin-bottom:1px}
/* ticks */
.ticks{list-style:none;position:absolute}
.ticks li{font-size:7px;color:#333;height:15.6px;display:flex;gap:6px}
.ticks li::before{content:"✓";color:#333;font-size:7px}
.sq li::before{content:"▪";color:var(--teal)}
.arrow-row{position:absolute;display:flex;gap:8px;align-items:flex-start}
.arrow-row span.ar{color:var(--blue);font-size:6px;line-height:1}
/* team */
.team-band{left:0;top:90px;width:372px;height:86px;background:var(--blue)}
.member{position:absolute;top:96px;width:80px;text-align:center;color:#fff}
.member .av{width:26px;height:26px;border-radius:50%;margin:0 auto 3px;background:radial-gradient(circle at 50% 40%,#e6cbb4,#8a6c58);border:2px solid #fff}
.member b{display:block;font:800 6px "Montserrat",sans-serif;color:#10243a;margin-bottom:2px}
.member p{font-size:3.2px;line-height:1.35;color:#e8f1f8}
/* timeline */
.tl-year{position:absolute;font:500 12px "Montserrat",sans-serif;color:#333;width:46px;text-align:center}
.tl-text{position:absolute;width:44px;text-align:center}
.tl-text b{display:block;font:700 4.2px "Montserrat",sans-serif;color:#333;margin-bottom:2px}
</style>
</head>
<body>

<!-- 01 Cover -->
<section class="slide c1 r1">
  <div class="photo cover-photo" role="img" aria-label="Soft blue DNA double helix background photograph"></div>
  <div class="abs cover-brand"><i></i>Corvane</div>
  <div class="abs head" style="left:44px;top:44px;font:600 9px Montserrat,sans-serif;color:var(--teal)">Biosciences</div>
  <div class="abs head" style="left:19px;top:108px;font-size:10px;color:var(--blue)">PRESENTATION</div>
  <div class="abs head bold" style="left:18px;top:120px;font-size:24px;color:var(--blue)">BUSINESS</div>
  <div class="abs head bold" style="left:18px;top:148px;font-size:23px;color:var(--teal)">MARKETING</div>
  <div class="abs" style="left:19px;top:178px;width:102px;height:1.5px;background:var(--teal)"></div>
  <div class="abs" style="left:19px;top:189px;font-size:6.5px;letter-spacing:2px;color:var(--blue-deep)">www.corvane.com</div>
</section>

<!-- 02 Contents -->
<section class="slide c2 r1">
  <div class="photo" style="left:0;top:0;width:183px;height:209px;background:linear-gradient(135deg,#8fb4d8,#3f74ab 60%,#1d4f86)" role="img" aria-label="Scientist holding a holographic DNA strand"></div>
  <div class="abs head" style="left:128px;top:96px;width:92px;height:24px;background:#fff;border-radius:12px 0 0 12px;font:700 16px/24px Montserrat,sans-serif;color:var(--teal);padding-left:4px">Contents</div>
  <svg class="abs" style="left:0;top:0" width="372" height="209"><path d="M228 45V193M222 108H228M228 45h4M228 80h4M228 122h4M228 157h4M228 193h4" stroke="#13a38b" stroke-width=".8" fill="none"/></svg>
  <div class="brand"><i></i>Corvane</div>
  <div class="toc-item tiny" style="top:40px"><b>Lorem ipsum</b>Lorem ipsum dolor sit amet, consectetuer adipiscing elit, sed diam nonummy nibh euismod tincid</div>
  <div class="toc-item tiny" style="top:75px"><b>Lorem ipsum</b>Lorem ipsum dolor sit amet, consectetuer adipiscing elit, sed diam nonummy nibh euismod tincid</div>
  <div class="toc-item tiny" style="top:117px"><b>Lorem ipsum</b>Lorem ipsum dolor sit amet, consectetuer adipiscing elit, sed diam nonummy nibh euismod tincid</div>
  <div class="toc-item tiny" style="top:152px"><b>Lorem ipsum</b>Lorem ipsum dolor sit amet, consectetuer adipiscing elit, sed diam nonummy nibh euismod tincid</div>
  <div class="pageno">02</div>
</section>

<!-- 03 Domain -->
<section class="slide c3 r1">
  <svg class="abs" style="left:0;top:0" width="372" height="209"><path d="M28 44V28H44M181 182V198H165" stroke="#0677ba" stroke-width="2.5" fill="none"/><path d="M181 182V198H165" stroke="#13a38b" stroke-width="2.5" fill="none"/></svg>
  <div class="photo" style="left:35px;top:34px;width:138px;height:140px;background:linear-gradient(145deg,#d8e8f6,#7badd7 55%,#b78f96 70%,#2f5f8f)" role="img" aria-label="Laboratory microscope with gloved hand"></div>
  <div class="brand"><i></i>Corvane</div>
  <div class="abs head" style="left:199px;top:32px;font-size:11px;color:var(--blue)">WHAT'S A DOMAIN?</div>
  <div class="abs head" style="left:199px;top:50px;font-size:11px;color:var(--blue)">IT'S THAT NAME UP</div>
  <div class="abs head bold" style="left:199px;top:66px;font-size:12.5px;color:var(--teal)">IN THE ADDRESS BAR.</div>
  <ul class="ticks" style="left:199px;top:89px">
    <li>Fits your business or products</li><li>Is easy to spell and remember</li><li>Fits your business or products</li><li>Is easy to spell and remember</li><li>Fits your business or products</li><li>Is easy to spell and remember</li>
  </ul>
  <div class="pageno">03</div>
</section>

<!-- 04 Two columns -->
<section class="slide c1 r2">
  <div class="abs" style="left:18px;top:18px;width:174px;height:174px;background:var(--grey-box)"></div>
  <div class="brand"><i></i>Corvane</div>
  <div class="abs head" style="left:31px;top:27px;font-size:11px;color:var(--blue)">LOREM IPSUM<br><span class="bold" style="color:var(--teal)">DOLOR SIT AMET</span></div>
  <div class="abs head" style="left:201px;top:27px;font-size:11px;color:var(--blue)">LOREM IPSUM<br><span class="bold" style="color:var(--teal)">DOLOR SIT AMET</span></div>
  <div class="abs small" style="left:31px;top:57px;width:156px;text-align:justify">Lorem ipsum dolor sit amet, consectetuer adipiscing elit, sed diam nonummy nibh euismod tincidunt ut laoreet dolore magna aliquam erat volutpat. Ut wisi enim ad minim veniam, quis nostrud exerci tation ullamcorper suscipit lobortis nisl ut aliquip ex ea commodo consequat. Duis autem vel eum iriure dolor in hendrerit in vulputate velit esse<br><br>Lorem ipsum dolor sit amet, consectetuer adipiscing elit, sed diam nonummy nibh euismod tincidunt ut laoreet dolore magna aliquam erat volutpat. Ut wisi enim ad minim veniam, quis nostrud exerci tation ullamcorper suscipit lobortis nisl ut aliquip ex ea commodo consequat. Duis autem vel eum iriure dolor in hendrerit in vulputate velit esse</div>
  <div class="abs small" style="left:201px;top:57px;width:156px;text-align:justify">Lorem ipsum dolor sit amet, consectetuer adipiscing elit, sed diam nonummy nibh euismod tincidunt ut laoreet dolore magna aliquam erat volutpat. Ut wisi enim ad minim veniam, quis nostrud exerci tation ullamcorper suscipit lobortis nisl ut aliquip ex ea commodo consequat. Duis autem vel eum iriure dolor in hendrerit in vulputate velit esse<br><br>Lorem ipsum dolor sit amet, consectetuer adipiscing elit, sed diam nonummy nibh euismod tincidunt ut laoreet dolore magna aliquam erat volutpat. Ut wisi enim ad minim veniam, quis nostrud exerci tation ullamcorper suscipit lobortis nisl ut aliquip ex ea commodo consequat. Duis autem vel eum iriure dolor in hendrerit in vulputate velit esse</div>
  <div class="arrow-row tiny" style="left:31px;top:144px;width:156px"><span class="ar">▶</span><span>Lorem ipsum dolor sit amet, consectetuer adipiscing elit, sed diam nonummy nibh euismod tincidunt ut laoreet dolore magna</span></div>
  <div class="arrow-row tiny" style="left:31px;top:167px;width:156px"><span class="ar">▷</span><span>Lorem ipsum dolor sit amet, consectetuer adipiscing elit, sed diam nonummy nibh euismod tincidunt ut laoreet dolore magna</span></div>
  <div class="arrow-row tiny" style="left:201px;top:144px;width:156px"><span class="ar">▶</span><span>Lorem ipsum dolor sit amet, consectetuer adipiscing elit, sed diam nonummy nibh euismod tincidunt ut laoreet dolore magna</span></div>
  <div class="arrow-row tiny" style="left:201px;top:167px;width:156px"><span class="ar">▷</span><span>Lorem ipsum dolor sit amet, consectetuer adipiscing elit, sed diam nonummy nibh euismod tincidunt ut laoreet dolore magna</span></div>
  <div class="pageno">04</div>
</section>

<!-- 05 Market opportunities -->
<section class="slide c2 r2">
  <div class="brand"><i></i>Corvane</div>
  <div class="abs head" style="left:19px;top:27px;font-size:13px;color:var(--blue)">MARKET<br><span class="bold" style="color:var(--teal)">OPPORTUNITIES</span></div>
  <div class="abs tiny" style="left:19px;top:63px;width:170px">Lorem ipsum dolor sit amet, consectetuer adipiscing elit, sed diam nonummy nibh euismod tincidunt ut laoreet dolore magna aliquam erat volutpat. Ut wisi enim ad minim veniam, quis nostrud exerci tation ullamcorper suscipit lobortis nisl ut aliquip ex ea commodo consequat. Duis autem vel eum iriure dolor in hendrerit i<br><br>Lorem ipsum dolor sit amet, consectetuer adipiscing elit, sed diam nonummy nibh euismod tincidunt ut laoreet dolore magna aliquam erat volutpat. Ut wisi enim ad minim veniam, quis nostrud exerci tation ullamcorper suscipit lobortis nisl ut aliquip ex</div>
  <svg class="abs" style="left:0;top:0" width="372" height="209" font-family="Montserrat,sans-serif">
    <text x="224" y="32" font-size="3.6" font-weight="700" fill="#222" text-anchor="middle">LOREM IPSUM</text>
    <text x="288" y="32" font-size="3.6" font-weight="700" fill="#222" text-anchor="middle">LOREM IPSUM</text>
    <circle cx="224" cy="63" r="24" fill="none" stroke="#0a9bd8" stroke-width="1"/>
    <path d="M204 76A24 24 0 0 0 246 74" fill="none" stroke="#13a38b" stroke-width="2.4"/>
    <circle cx="288" cy="63" r="24" fill="none" stroke="#0a9bd8" stroke-width="1"/>
    <path d="M272 80A24 24 0 0 0 311 68" fill="none" stroke="#13a38b" stroke-width="2.4"/>
    <text x="224" y="66" font-size="9" font-weight="800" fill="#222" text-anchor="middle" letter-spacing="2">4356</text>
    <text x="288" y="66" font-size="9" font-weight="800" fill="#222" text-anchor="middle" letter-spacing="2">2164</text>
    <text x="224" y="72" font-size="2" fill="#555" text-anchor="middle">LOREM IPSUM</text>
    <text x="288" y="72" font-size="2" fill="#555" text-anchor="middle">LOREM IPSUM</text>
    <g font-size="3.4" fill="#888"><text x="20" y="119">1000</text><text x="21" y="132">700</text><text x="21" y="145">500</text><text x="21" y="158">300</text><text x="21" y="172">100</text><text x="22" y="186">0</text></g>
    <path d="M36 116V186H195" stroke="#aaa" stroke-width=".4" fill="none"/>
    <path d="M36 186C46 176 55 168 62 170C70 172 75 182 80 178C88 170 92 158 100 158C108 158 112 172 120 172C128 172 130 140 140 136C150 132 154 168 165 170C175 172 180 172 192 186Z" fill="#0a9bd8"/>
    <g font-size="4.4" font-weight="700" fill="#13a38b"><text x="49" y="165">100</text><text x="69" y="176">20</text><text x="97" y="152">275</text><text x="113" y="166">130</text><text x="141" y="131">650</text><text x="178" y="169">80</text></g>
    <g stroke="#ccc" stroke-width=".3">
      <path d="M217 118H322M217 128H322M217 138H322M217 148H322M217 158H322M217 168H322M217 178H322"/>
      <path d="M227 116V186M237 116V186M247 116V186M257 116V186M267 116V186M277 116V186M287 116V186M297 116V186M307 116V186M317 116V186"/>
    </g>
    <path d="M217 116V186H322" stroke="#555" stroke-width=".4" fill="none"/>
    <g fill="none" stroke="#13a38b" stroke-width=".8">
      <path d="M218 184C224 150 232 135 246 130C262 124 272 124 286 128C300 132 310 118 322 117"/>
      <path d="M218 184C224 160 232 145 246 139C262 133 276 124 290 130C302 136 312 122 322 123"/>
      <path d="M218 184C225 165 234 155 246 151C262 146 280 152 292 150C304 148 312 136 322 130"/>
      <path d="M218 184C226 170 235 162 246 160C262 157 278 158 292 166C304 172 314 162 322 160"/>
      <path d="M218 184C226 178 234 172 246 170C262 168 280 178 292 175C306 172 314 145 322 136"/>
    </g>
    <g fill="#13a38b"><circle cx="246" cy="130" r="1.2"/><circle cx="246" cy="139" r="1.2"/><circle cx="246" cy="151" r="1.2"/><circle cx="246" cy="160" r="1.2"/><circle cx="246" cy="170" r="1.2"/><circle cx="322" cy="117" r="1.2"/><circle cx="322" cy="123" r="1.2"/><circle cx="322" cy="130" r="1.2"/><circle cx="322" cy="136" r="1.2"/><circle cx="322" cy="160" r="1.2"/></g>
    <rect x="246" y="119" width="26" height="6" fill="#13a38b"/>
    <text x="259" y="123.3" font-size="3.4" font-weight="700" fill="#fff" text-anchor="middle">TEXT HERE</text>
  </svg>
  <div class="pageno">05</div>
</section>

<!-- 06 Company overview -->
<section class="slide c3 r2">
  <div class="brand"><i></i>Corvane</div>
  <div class="abs head bold" style="left:23px;top:23px;font-size:13px;color:var(--teal)">COMPANY<br><span style="font-size:19px">OVERVIEW</span></div>
  <div class="abs tiny" style="left:23px;top:63px;width:150px">Lorem ipsum dolor sit amet, consectetuer adipiscing elit, sed diam nonummy nibh euismod tincidunt ut laoreet dolore magna aliquam erat volutpat. Ut wisi enim ad minim veniam, quis nostrud exerci tation ullamcorper suscipit lobortis nisl ut aliquip ex ea commodo consequat. Duis autem vel eum iriure dolor in hendrerit i<br><br>Lorem ipsum dolor sit amet, consectetuer adipiscing elit, sed diam nonummy nibh</div>
  <svg class="abs" style="left:0;top:0" width="372" height="209" font-family="Montserrat,sans-serif">
    <g font-size="4.4" fill="#333" text-anchor="end"><text x="194" y="40">60</text><text x="194" y="52">50</text><text x="194" y="63">40</text><text x="194" y="75">30</text><text x="194" y="87">20</text><text x="194" y="99">10</text><text x="194" y="111">0</text></g>
    <rect x="197" y="38" width="153" height="71" fill="none" stroke="#ccc" stroke-width=".4"/>
    <g stroke="#ddd" stroke-width=".3"><path d="M197 50H350M197 62H350M197 73H350M197 85H350M197 97H350"/></g>
    <g fill="#0a9bd8"><rect x="210" y="62" width="4" height="47"/><rect x="243" y="96" width="4" height="13"/><rect x="275" y="41" width="4" height="68"/><rect x="307" y="48" width="4" height="61"/></g>
    <g fill="#13a38b"><rect x="215" y="50" width="4" height="59"/><rect x="248" y="68" width="4" height="41"/><rect x="280" y="93" width="4" height="16"/><rect x="312" y="74" width="4" height="35"/></g>
    <g font-size="5" fill="#333" text-anchor="middle"><text x="214" y="117">JAN</text><text x="247" y="117">FEB</text><text x="279" y="117">MAR</text><text x="311" y="117">APR</text></g>
    <g font-size="3.6" fill="#333" text-anchor="end"><text x="18" y="127">60</text><text x="18" y="136">50</text><text x="18" y="145">40</text><text x="18" y="155">30</text><text x="18" y="164">20</text><text x="18" y="173">10</text><text x="18" y="182">0</text></g>
    <path d="M20 125H179M20 181H179" stroke="#333" stroke-width=".4"/>
    <g font-size="2.2" fill="#333" text-anchor="middle"><text x="41" y="186">TEXT 01</text><text x="57" y="186">TEXT 02</text><text x="72" y="186">TEXT 03</text><text x="88" y="186">TEXT 04</text><text x="103" y="186">TEXT 05</text><text x="119" y="186">TEXT 06</text><text x="134" y="186">TEXT 07</text><text x="150" y="186">TEXT 08</text><text x="165" y="186">TEXT 09</text></g>
    <polyline points="41,181 57,172 72,155 88,136 103,147 119,156 134,165 150,146 165,172" fill="none" stroke="#0a9bd8" stroke-width=".7"/>
    <polyline points="41,168 57,178 72,164 88,163 103,146 119,164 134,155 150,160 165,146" fill="none" stroke="#0a9bd8" stroke-width=".7"/>
    <g fill="#0a9bd8"><circle cx="57" cy="172" r=".9"/><circle cx="72" cy="155" r=".9"/><circle cx="88" cy="136" r=".9"/><circle cx="103" cy="147" r=".9"/><circle cx="119" cy="156" r=".9"/><circle cx="134" cy="165" r=".9"/><circle cx="150" cy="146" r=".9"/><circle cx="41" cy="168" r=".9"/><circle cx="57" cy="178" r=".9"/><circle cx="88" cy="163" r=".9"/><circle cx="165" cy="146" r=".9"/></g>
    <g fill="#0a9bd8"><circle cx="194" cy="138" r="2.6"/><circle cx="284" cy="138" r="2.6"/><circle cx="194" cy="164" r="2.6"/><circle cx="284" cy="164" r="2.6"/></g>
    <g font-size="5" font-weight="600" fill="#0a9bd8"><text x="200" y="140">Lorem ipsum</text><text x="290" y="140">Lorem ipsum</text><text x="200" y="166">Lorem ipsum</text><text x="290" y="166">Lorem ipsum</text></g>
    <g font-size="2.6" fill="#777"><text x="200" y="146">Lorem ipsum dolor sit amet, consec</text><text x="200" y="150">tetuer adipiscing elit, sed diam</text><text x="290" y="146">Lorem ipsum dolor sit amet, consec</text><text x="290" y="150">tetuer adipiscing elit, sed diam</text><text x="200" y="172">Lorem ipsum dolor sit amet, consec</text><text x="200" y="176">tetuer adipiscing elit, sed diam</text><text x="290" y="172">Lorem ipsum dolor sit amet, consec</text><text x="290" y="176">tetuer adipiscing elit, sed diam</text></g>
  </svg>
  <div class="pageno">06</div>
</section>

<!-- 07 Active intelligence -->
<section class="slide c1 r3">
  <div class="brand"><i></i>Corvane</div>
  <div class="abs head" style="left:19px;top:20px;font-size:13px;color:var(--blue)">ACTIVE<br><span class="bold" style="color:var(--teal)">INTELLIGENCE</span></div>
  <div class="abs small" style="left:19px;top:52px;width:150px;text-align:justify">Lorem ipsum dolor sit amet, consectetuer adipiscing elit, sed diam nonummy nibh euismod tincidunt ut laoreet dolore magna aliquam erat volutpat. Ut wisi enim ad minim veniam, quis nostrud exerci tation ullamcorper suscipit lobortis nisl ut aliquip ex ea commodo consequat. Duis autem vel eum iriure dolor in hendrerit in vulputate velit esse<br><br>Lorem ipsum dolor sit amet, consectetuer adipiscing elit, sed diam nonummy nibh euismod tincidunt ut laoreet dolore magna aliquam erat volutpat. Ut wisi enim ad minim veniam, quis nostrud exerci tation ullamcorper suscipit lobortis nisl ut aliquip ex ea commodo consequat. Duis autem vel eum iriure dolor in hendrerit in vulputate velit esse</div>
  <div class="arrow-row tiny" style="left:19px;top:146px;width:150px"><span class="ar">▶</span><span>Lorem ipsum dolor sit amet, consectetuer adipiscing elit, sed diam nonummy nibh euismod tincidunt ut laoreet dolore magna</span></div>
  <div class="arrow-row tiny" style="left:19px;top:170px;width:150px"><span class="ar">▷</span><span>Lorem ipsum dolor sit amet, consectetuer adipiscing elit, sed diam nonummy nibh euismod tincidunt ut laoreet dolore magna</span></div>
  <div class="abs" style="left:262px;top:33px;width:80px;height:2.5px;background:var(--blue)"></div>
  <div class="abs" style="left:178px;top:137px;width:2px;height:58px;background:var(--teal)"></div>
  <div class="abs" style="left:178px;top:193px;width:100px;height:2px;background:var(--teal)"></div>
  <div class="photo" style="left:184px;top:40px;width:188px;height:136px;background:linear-gradient(120deg,#cfe3f3,#6fa3cf 45%,#2c6a9e 75%,#dde9f3)" role="img" aria-label="Researcher in lab cap using a digital interface of medical icons"></div>
  <div class="pageno">07</div>
</section>

<!-- 08 Diagram -->
<section class="slide c2 r3">
  <div class="brand"><i></i>Corvane</div>
  <div class="abs head bold" style="left:25px;top:32px;font-size:17.5px;color:var(--teal)">LOREM IPSUM<br>DOLOR SIT AMET</div>
  <div class="abs tiny" style="left:228px;top:49px;width:130px">Lorem ipsum dolor sit amet, consectetuer adipiscing elit, sed diam nonummy nibh euismod tincidunt ut laoreet dolore magna aliquam erat volutpat. Ut wisi enim ad minim veniam, quis nostrud exerci tation ullamcorper suscipit lobortis nisl ut aliquip ex ea commodo consequat. Duis autem vel eum</div>
  <svg class="abs" style="left:0;top:0" width="372" height="209" font-family="Montserrat,sans-serif">
    <g stroke="#13a38b" stroke-width="2.2" fill="none"><path d="M107 125Q112 140 130 150"/><path d="M146 125Q146 136 142 140"/><path d="M173 125Q172 136 160 140"/><path d="M210 125Q206 140 188 150"/></g>
    <circle cx="107" cy="117" r="12" fill="#13a38b"/><circle cx="148" cy="108" r="12" fill="#13a38b"/><circle cx="178" cy="108" r="12" fill="#13a38b"/><circle cx="210" cy="117" r="12" fill="#13a38b"/>
    <circle cx="159" cy="155" r="17" fill="none" stroke="#13a38b" stroke-width="4" stroke-dasharray="6 2"/>
    <circle cx="159" cy="155" r="11" fill="#fff" stroke="#13a38b" stroke-width=".8"/>
    <text x="159" y="157" font-size="4" font-weight="700" fill="#13a38b" text-anchor="middle">Corvane</text>
    <g fill="#fff" font-size="3.2" font-weight="600" text-anchor="middle"><text x="107" y="124">Option A</text><text x="148" y="115">Option B</text><text x="178" y="115">Option C</text><text x="210" y="124">Option D</text></g>
    <g fill="#fff"><rect x="103" y="111" width="8" height="5" rx="1"/><rect x="144" y="102" width="8" height="5" rx="1"/><rect x="174" y="102" width="8" height="5" rx="1"/><rect x="206" y="111" width="8" height="5" rx="1"/></g>
    <g font-size="4" font-weight="600" fill="#0a9bd8"><text x="46" y="100">Your Title</text><text x="145" y="97">Your Title</text><text x="21" y="134">Your Title</text><text x="171" y="129">Your Title</text></g>
    <g font-size="2.2" fill="#888"><text x="45" y="105">Add your short note</text><text x="45" y="108">about this option</text><text x="145" y="102">Add your short note</text><text x="145" y="105">about this option</text><text x="18" y="139">Add your short note</text><text x="18" y="142">about this option</text><text x="171" y="134">Add your short note</text><text x="171" y="137">about this option</text></g>
    <circle cx="241" cy="107" r="13" fill="none" stroke="#0a9bd8" stroke-width=".6"/>
    <circle cx="241" cy="146" r="13" fill="none" stroke="#0a9bd8" stroke-width=".6"/>
    <path d="M233 106L241 102L249 106L241 110Z M237 108V112H245V108" fill="#0677ba"/>
    <path d="M234 141H248V150H234Z M236 152H246" stroke="#0677ba" stroke-width="1" fill="none"/>
    <g font-size="5.2" font-weight="600" fill="#0a9bd8"><text x="262" y="102">LOREM IPSUM</text><text x="262" y="141">LOREM IPSUM</text></g>
  </svg>
  <div class="abs tiny" style="left:262px;top:104px;width:66px">Lorem ipsum dolor sit amet, consectetuer adipiscing elit, sed diam nonummy nibh euismod tincid</div>
  <div class="abs tiny" style="left:262px;top:143px;width:66px">Lorem ipsum dolor sit amet, consectetuer adipiscing elit, sed diam nonummy nibh euismod tincid</div>
  <div class="pageno">08</div>
</section>

<!-- 09 Lists -->
<section class="slide c3 r3">
  <div class="brand"><i></i>Corvane</div>
  <div class="abs head" style="left:18px;top:36px;font-size:13px;color:var(--blue)">LOREM IPSUM<br><span class="bold" style="color:var(--teal)">DOLOR SIT AMET</span></div>
  <div class="abs" style="left:18px;top:72px;width:175px;font-size:5px;line-height:1.15;color:#444">
    <p style="margin-bottom:8px"><b class="t-blue">• Lorem ipsum :</b> dolor sit amet, consectetuer adipiscing elit, nonummy nibh euismod tincidunt ut laoreet dolore magna</p>
    <p style="margin-bottom:8px"><b class="t-blue">• Lorem ipsum :</b> dolor sit amet, consectetuer adipiscing elit, sed diam nonummy nibh euismod tincidunt ut laoreet dolore magna aliquam erat volutpat. Ut wisi enim ad min, quis nostrud exerci tation ullamcorper suscipit lobortis nisl</p>
    <p style="margin-bottom:8px"><b class="t-blue">• Lorem ipsum :</b> dolor sit amet, consectetuer adipis cing elit, sed diam nonummy nibh euismod tinci dunt ut laoreet magna aliquam erat volutpat.</p>
    <p style="margin-bottom:8px"><b class="t-blue">• Lorem ipsum :</b> dolor sit amet, consectetuer adipiscing nibh euismod tincidunt ut laoreet dolore magna</p>
    <p><b class="t-blue">• Lorem ipsum :</b> dolor sit amet, consectetuer adipis cing elit, sed diam nonummy nibh euismod tinci dunt ut laoreet dolore.</p>
  </div>
  <div class="abs head" style="left:210px;top:36px;font-size:11px;color:var(--blue)">WHAT'S A DOMAIN?</div>
  <div class="abs head" style="left:210px;top:52px;font-size:11px;color:var(--blue)">IT'S THAT NAME UP</div>
  <div class="abs head bold" style="left:210px;top:67px;font-size:12.5px;color:var(--teal)">IN THE ADDRESS BAR.</div>
  <ul class="ticks sq" style="left:210px;top:91px">
    <li style="font-size:8.5px;height:16.2px">Fits your business or products</li><li style="font-size:8.5px;height:16.2px">Is easy to spell and remember</li><li style="font-size:8.5px;height:16.2px">Fits your business or products</li><li style="font-size:8.5px;height:16.2px">Is easy to spell and remember</li><li style="font-size:8.5px;height:16.2px">Fits your business or products</li><li style="font-size:8.5px;height:16.2px">Is easy to spell and remember</li>
  </ul>
  <div class="pageno">09</div>
</section>

<!-- 10 Timeline -->
<section class="slide c1 r4">
  <div class="brand"><i></i>Corvane</div>
  <div class="abs head" style="left:68px;top:22px;font:500 13px Montserrat,sans-serif;letter-spacing:4px;color:var(--teal)">TIMELINE</div>
  <div class="abs head" style="left:163px;top:21px;background:var(--teal);color:#fff;font:700 13px/17px Montserrat,sans-serif;letter-spacing:3.5px;padding:0 4px">INFOGRAPHIC</div>
  <svg class="abs" style="left:0;top:0" width="372" height="209">
    <path d="M52 121H321" stroke="#999" stroke-width=".6"/>
    <g fill="none" stroke="#13a38b" stroke-width="1.6">
      <path d="M65 121V88Q65 83 70 83H109Q114 83 114 88V121"/>
      <path d="M164 121V88Q164 83 169 83H208Q213 83 213 88V121"/>
      <path d="M262 121V88Q262 83 267 83H303Q308 83 308 88V121"/>
      <path d="M114 121V148Q114 153 119 153H158Q163 153 163 148V121"/>
      <path d="M213 121V148Q213 153 218 153H257Q262 153 262 148V121"/>
    </g>
    <g fill="#0a9bd8" stroke="#fff" stroke-width="1.5"><circle cx="89" cy="83" r="7"/><circle cx="188" cy="83" r="7"/><circle cx="285" cy="83" r="7"/></g>
    <g fill="#13a38b" stroke="#fff" stroke-width="1.5"><circle cx="138" cy="153" r="7"/><circle cx="237" cy="153" r="7"/></g>
    <g fill="#0a9bd8"><rect x="132" y="57" width="8" height="8" rx="1"/><rect x="230" y="57" width="8" height="8" rx="1"/><rect x="85" y="125" width="8" height="8" rx="4"/><rect x="184" y="125" width="8" height="8" rx="4"/><rect x="281" y="125" width="8" height="8" rx="1"/></g>
  </svg>
  <div class="tl-year" style="left:66px;top:99px">2018</div>
  <div class="tl-year" style="left:165px;top:99px">2020</div>
  <div class="tl-year" style="left:262px;top:99px">2022</div>
  <div class="tl-year" style="left:115px;top:128px">2029</div>
  <div class="tl-year" style="left:214px;top:128px">2021</div>
  <div class="tl-text tiny" style="left:116px;top:67px"><b>LOREM IPSUM</b>Lorem ipsum dolor sit amet, consectetur adipiscing elit. Duis elit sapien, convallis vel enim sit amet, egestas commodo arcu.</div>
  <div class="tl-text tiny" style="left:215px;top:67px"><b>LOREM IPSUM</b>Lorem ipsum dolor sit amet, consectetur adipiscing elit. Duis elit sapien, convallis vel enim sit amet, egestas commodo arcu.</div>
  <div class="tl-text tiny" style="left:67px;top:136px"><b>LOREM IPSUM</b>Lorem ipsum dolor sit amet, consectetur adipiscing elit. Duis elit sapien, convallis vel enim sit amet, egestas commodo arcu.</div>
  <div class="tl-text tiny" style="left:166px;top:136px"><b>LOREM IPSUM</b>Lorem ipsum dolor sit amet, consectetur adipiscing elit. Duis elit sapien, convallis vel enim sit amet, egestas commodo arcu.</div>
  <div class="tl-text tiny" style="left:263px;top:136px"><b>LOREM IPSUM</b>Lorem ipsum dolor sit amet, consectetur adipiscing elit. Duis elit sapien, convallis vel enim sit amet, egestas commodo arcu.</div>
  <div class="pageno">10</div>
</section>

<!-- 11 Team -->
<section class="slide c2 r4">
  <div class="brand"><i></i>Corvane</div>
  <div class="abs head" style="left:0;width:372px;text-align:center;top:32px;font-size:11.5px;font-weight:600;color:var(--teal)">TEAM MEMBERS <span class="bold">AND ADVISORS</span></div>
  <div class="abs tiny" style="left:22px;top:50px;width:328px;text-align:center;font-size:4.2px">Lorem ipsum dolor sit amet, consectetuer adipiscing elit, sed diam nonummy nibh euismod tincidunt ut laoreet dolore magna aliquam erat volutpat. Ut wisi enim ad minim veniam, quis nostrud exerci tation ullamcorper suscipit lobortis nisl ut aliquip ex ea commodo consequat. Duis autem<br><br>Lorem ipsum dolor sit amet, cons ectetuer adipiscing elit, sed diam nonummy nibh euismod tincidunt ut laoreet dolore magna aliquam erat volutpat.</div>
  <div class="abs team-band"></div>
  <div class="member" style="left:12px"><div class="av" role="img" aria-label="Portrait photo of team member"></div><b>OWEN HALE</b><p>Chief executive leading strategy, fundraising and partnerships across our research programs.</p></div>
  <div class="member" style="left:102px"><div class="av" role="img" aria-label="Portrait photo of team member"></div><b>IRIS MOREAU</b><p>Scientific officer guiding lab discovery, assay design and our early clinical roadmap.</p></div>
  <div class="member" style="left:189px"><div class="av" role="img" aria-label="Portrait photo of advisor"></div><b>OWEN HALE</b><p>Board advisor with long experience in biotech finance and growth-stage investment.</p></div>
  <div class="member" style="left:278px"><div class="av" role="img" aria-label="Portrait photo of advisor"></div><b>IRIS MOREAU</b><p>Regulatory advisor supporting trial planning, approvals and quality systems.</p></div>
  <div class="pageno">11</div>
</section>

<!-- 12 Thank you -->
<section class="slide c3 r4">
  <div class="abs" style="left:34px;top:82px;display:flex;align-items:center;gap:5px;font:700 20px/1 Montserrat,sans-serif;color:var(--teal)"><i style="width:14px;height:14px;border-radius:50%;background:var(--teal);display:block"></i>Corvane</div>
  <div class="abs" style="left:53px;top:104px;font:600 8px Montserrat,sans-serif;color:var(--teal)">Biosciences</div>
  <div class="abs head bold" style="left:161px;top:68px;font-size:16.5px;color:#222">THANK YOU</div>
  <div class="abs head bold" style="left:161px;top:94px;font-size:10px;color:var(--teal)">CONTACT US</div>
  <svg class="abs" style="left:161px;top:109px" width="6" height="30"><circle cx="3" cy="3" r="2.4" fill="#13a38b"/><circle cx="3" cy="12" r="2.4" fill="#13a38b"/><circle cx="3" cy="21" r="2.4" fill="#13a38b"/></svg>
  <div class="abs" style="left:170px;top:108px;font-size:6.4px;line-height:9px;color:#222">555-014-2208<br>info@corvanebio.com<br>Your address, your city, box 88900</div>
</section>

</body>
</html>
```